New Company Business Card design

Looking for a corporate looking business card utilising my new logo design - the logo i would like embossed as one option and flat as another - simplistic but stylish - less is more - we are an import export business launching into the market - i would like a couple of options as main background - Grey or Black

```html
<!DOCTYPE html>
<html lang="en">
<head>
<meta charset="utf-8">
<title>Meridian Trade Partners – Business Card</title>
<link rel="stylesheet" href="https://fonts.googleapis.com/css2?family=Cinzel:wght@500&family=Arimo&display=swap">
<style>
  :root {
    --stage: #666666;
    --card-grey: #696a6f;
    --brand-blue: #1c75bc;
    --paper: #ffffff;
    --ink-light: #ffffff;
  }
  html, body {
    margin: 0;
    width: 1200px;
    height: 802px;
    overflow: hidden;
    background: var(--stage);
  }
  .stage {
    position: relative;
    width: 1200px;
    height: 802px;
  }
  .card {
    position: absolute;
    top: 274px;
    width: 443px;
    height: 265px;
    display: block;
  }
  .card--front { left: 135px; }
  .card--back { left: 624px; }
  .bg-grey { fill: var(--card-grey); }
  .bg-blue { fill: var(--brand-blue); }
  .bg-paper { fill: var(--paper); }
  .holder-name {
    font-family: "Cinzel", serif;
    font-weight: 500;
    font-size: 24px;
    fill: var(--ink-light);
  }
  .holder-role, .contact-line {
    font-family: "Arimo", sans-serif;
    fill: var(--ink-light);
  }
  .holder-role { font-size: 15.5px; }
  .contact-line { font-size: 15.5px; }
  .contact-icon { fill: var(--ink-light); }
  .company-name {
    font-family: "Cinzel", serif;
    font-weight: 500;
    font-size: 24px;
    fill: var(--brand-blue);
    letter-spacing: 0.5px;
  }
</style>
</head>
<body>
<main class="stage">

  <svg class="card card--front" viewBox="0 0 546 326" aria-label="Business card front">
    <rect class="bg-blue" width="546" height="326"/>
    <rect class="bg-grey side-band" width="62" height="326"/>

    <text class="holder-name" x="510" y="168" text-anchor="end">Daniel Brooke</text>
    <text class="holder-role" x="510" y="186" text-anchor="end">Managing Director</text>

    <g class="contact-list">
      <text class="contact-line" x="492" y="230" text-anchor="end">044-555 010 234</text>
      <path class="contact-icon" d="M496,224 q7,-5 14,0 v2 h-3 v-1 h-8 v1 h-3 z M498,226 h10 v4 h-10 z"/>

      <text class="contact-line" x="492" y="249" text-anchor="end">044-555 010 876</text>
      <rect x="499" y="238" width="7" height="12" rx="1.2" fill="none" stroke="#fff" stroke-width="1.4"/>

      <text class="contact-line" x="492" y="269" text-anchor="end">hello@meridiantrade.example</text>
      <rect class="contact-icon" x="497" y="260" width="11" height="8"/>
      <path d="M497,260 l5.5,4.5 l5.5,-4.5" fill="none" stroke="#1c75bc" stroke-width="1"/>

      <text class="contact-line" x="492" y="289" text-anchor="end">www.meridiantrade.example</text>
      <circle class="contact-icon" cx="502.5" cy="284" r="5.5"/>
      <path d="M499,282 q3,-2 5,1 q-1,3 2,4" fill="none" stroke="#1c75bc" stroke-width="1.2"/>
    </g>
  </svg>

  <svg class="card card--back" viewBox="0 0 546 326" aria-label="Business card back">
    <rect class="bg-paper" width="546" height="326"/>
    <text class="company-name" x="273" y="172" text-anchor="middle">Meridian Trade Partners</text>
  </svg>

</main>
</body>
</html>
```